Larkfield Prose Studio (LPStudio.net)

We need a Wordpress-based site designed for a client who provides writing and editing services for the IT industry. We have a wireframe complete for the homepage, but need all internal pages designed (based on homepage wireframe) and the entire site coded for WP.

Internal pages include: "Our Work" (with samples & testimonials); "Capabilities" (with sections to address "strategy", "coaching", "writing" and "editing"); "About Us"; and a Contact page.

Will provide all copywriting, writing samples, testimonials, and client logos.

We completely realize/acknowledge the subject matter is visually BORING! Anything at all that can be done to make it look visually appealing would be *great*! Stock photography is fine.

Please feel free to ask any questions whatsoever. Thanks for your time!

```html
<!DOCTYPE html>
<html lang="en">
<head>
<meta charset="utf-8">
<title>Larkfield Prose Studio</title>
<link rel="stylesheet" href="https://fonts.googleapis.com/css2?family=Poppins:wght@400;500;600&display=swap">
<style>
:root{
  --green:#4caf50;
  --green-band:#55b565;
  --blue:#1d73c4;
  --blue-band:#0f78cf;
  --ink:#111;
  --muted:#555;
  --hero-bg:#f3f3f3;
  --line:#e6e6e6;
  --purple:#4b3a8c;
}
*{box-sizing:border-box;margin:0;padding:0}
html,body{width:1200px;height:3367px;overflow:hidden}
body{font-family:"Poppins",sans-serif;color:var(--ink);background:#fff;position:relative}
.abs{position:absolute}
.btn{position:absolute;background:var(--green);color:#fff;font-weight:500;font-size:16px;display:flex;align-items:center;justify-content:center;border-radius:2px}

/* header + hero */
.hero{position:absolute;left:0;top:0;width:1200px;height:656px;background:var(--hero-bg)}
.wordmark{font-weight:600;font-size:24px;line-height:26px;color:var(--green)}
.nav{position:absolute;top:34px;left:458px;display:flex;gap:32px;font-size:15px;font-weight:500}
.hero h1{position:absolute;left:102px;top:262px;width:460px;font-size:44px;line-height:47px;font-weight:600;color:var(--blue)}
.hero h1 span{color:var(--green)}
.hero-photo{position:absolute;left:640px;top:106px;width:380px;height:494px;border-radius:190px 190px 40px 40px;background:linear-gradient(180deg,#d9d3cc,#8ea0bb 55%,#c9c9c9)}
.ring{position:absolute;border:1px solid #e2e2e2;border-radius:50%}
.badge{position:absolute;width:88px;height:88px;border-radius:50%;background:#fff;box-shadow:0 2px 10px rgba(0,0,0,.08);display:flex;flex-direction:column;align-items:center;justify-content:center;font-size:12px;font-weight:500;gap:6px}
.badge i{display:block;width:26px;height:24px;border:2px solid #333;border-radius:3px}

/* section headings */
.sec-head{position:absolute;left:0;width:1200px;text-align:center;font-size:31px;line-height:38px;font-weight:500}
.sec-head span{display:block;color:var(--green)}

/* service cards */
.svc{position:absolute;top:856px;width:236px;height:318px;background:#fff;box-shadow:0 2px 10px rgba(0,0,0,.07);text-align:center}
.svc .ph{height:168px}
.svc h3{font-size:20px;font-weight:500;margin-top:20px}
.svc p{font-size:12.5px;color:var(--muted);line-height:21px;padding:6px 16px 0}
.svc .bar{position:absolute;bottom:0;left:72px;width:76px;height:3px;background:linear-gradient(90deg,var(--purple) 50%,var(--green) 50%)}

/* clients band */
.clients{position:absolute;left:0;top:1362px;width:1200px;height:625px;background:var(--green-band)}
.clients h2{position:absolute;top:98px;width:1200px;text-align:center;color:#fff;font-size:35px;font-weight:500}
.client{position:absolute;width:163px;height:163px;margin:-81px 0 0 -81px;border-radius:50%;background:#fff;display:flex;align-items:center;justify-content:center;gap:7px;font-weight:600;font-size:20px;color:#222}
.client i{width:14px;height:14px;border-radius:50%;background:#333}

/* case cards */
.case{position:absolute;top:2176px;width:316px;height:401px;border:1px solid var(--line);background:#fff}
.case .ph{height:203px}
.case .tag{position:absolute;left:56px;top:180px;width:204px;height:48px;background:#f2f2f2;display:flex;align-items:center;justify-content:center;gap:8px;font-weight:600;font-size:16px;letter-spacing:.5px}
.case .tag i{width:20px;height:20px;background:#e86c3a}
.case h3{font-size:19px;font-weight:500;line-height:25px;padding:44px 14px 10px}
.case hr{border:0;border-top:1px solid var(--line);margin:0 12px}
.case p{font-size:12.5px;color:var(--muted);line-height:20px;padding:12px 16px}

/* contact band */
.contact{position:absolute;left:0;top:2666px;width:1200px;height:408px;background:var(--blue-band);color:#fff}
.contact h2{position:absolute;top:122px;width:420px;text-align:center;font-size:25px;font-weight:500;line-height:38px}
.contact .divider{position:absolute;left:605px;top:110px;width:1px;height:190px;background:rgba(255,255,255,.35)}
.email{position:absolute;left:688px;top:230px;width:350px;height:47px;background:#fff;color:#555;font-size:13px;display:flex;align-items:center;padding:0 24px;justify-content:space-between}

/* footer */
.footer-col h4{font-size:18px;font-weight:500}
.footer-col li{list-style:none;font-size:12.5px;line-height:20px;display:flex;gap:6px;align-items:flex-start}
.social{display:flex;gap:10px}
.social span{width:34px;height:34px;border-radius:50%;background:#222}
.copy{position:absolute;left:0;top:3294px;width:1200px;height:73px;background:#eee;font-size:13px;display:flex;align-items:center;justify-content:center}
</style>
</head>
<body>

<section class="hero">
  <div class="wordmark abs" style="left:100px;top:20px">Larkfield Prose<br>Studio</div>
  <nav class="nav"><span>Home</span><span>Our Work ⌄</span><span>Capabilities ⌄</span><span>About Us</span><span>Blog</span></nav>
  <div class="btn" style="left:958px;top:24px;width:140px;height:45px">Get In Touch</div>

  <h1><span>Communicate your</span> expertise and your customer successes</h1>
  <div class="btn" style="left:100px;top:434px;width:140px;height:44px">Get Started</div>

  <div class="ring" style="left:592px;top:130px;width:480px;height:480px"></div>
  <div class="ring" style="left:632px;top:170px;width:400px;height:400px"></div>
  <div class="hero-photo" role="img" aria-label="Smiling writer sitting cross-legged holding a laptop"></div>
  <div class="badge" style="left:619px;top:178px"><i></i>Strategy</div>
  <div class="badge" style="left:946px;top:178px"><i></i>Coaching</div>
  <div class="badge" style="left:584px;top:403px"><i></i>Writing</div>
  <div class="badge" style="left:981px;top:403px"><i></i>Editing</div>
</section>

<h2 class="sec-head" style="top:744px">Text copy that explains in concise, snappy terms<span>the value you provide to customers.</span></h2>

<article class="svc" style="left:99px"><div class="ph" role="img" aria-label="Team reviewing charts on a desk" style="background:linear-gradient(135deg,#cfd6dc,#8a96a3)"></div><h3>Strategy</h3><p>Loremolor sit amet, consectetur adipiscing elit, sed do eiusmod tempor incididunt ut</p><span class="bar"></span></article>
<article class="svc" style="left:354px"><div class="ph" role="img" aria-label="Coach in a suit at a laptop" style="background:linear-gradient(135deg,#9a8a76,#37465e)"></div><h3>Coaching</h3><p>Loremolor sit amet, consectetur adipiscing elit, sed do eiusmod tempor incididunt ut</p><span class="bar"></span></article>
<article class="svc" style="left:609px"><div class="ph" role="img" aria-label="Hands writing in a notebook next to a laptop" style="background:linear-gradient(135deg,#c9a27a,#6d4d33)"></div><h3>Writing</h3><p>Loremolor sit amet, consectetur adipiscing elit, sed do eiusmod tempor incididunt ut</p><span class="bar"></span></article>
<article class="svc" style="left:864px"><div class="ph" role="img" aria-label="Editor marking printed pages by a window" style="background:linear-gradient(135deg,#e8c68a,#c4c8d4)"></div><h3>Editing</h3><p>Loremolor sit amet, consectetur adipiscing elit, sed do eiusmod tempor incididunt ut</p><span class="bar"></span></article>

<div class="btn" style="left:490px;top:1221px;width:220px;height:46px">View Our Capabilities</div>

<section class="clients">
  <h2>A selection of past &amp; current clients</h2>
  <div class="client" style="left:225px;top:261px"><i></i>Norvale</div>
  <div class="client" style="left:413px;top:261px"><i></i>quartzen</div>
  <div class="client" style="left:600px;top:261px"><i></i>Caldwin</div>
  <div class="client" style="left:787px;top:261px"><i></i>ostra.</div>
  <div class="client" style="left:974px;top:261px"><i></i>Pellow</div>
  <div class="client" style="left:333px;top:438px"><i></i>arcwell</div>
  <div class="client" style="left:520px;top:438px"><i></i>TAVENO</div>
  <div class="client" style="left:708px;top:438px"><i></i>LUMERA</div>
  <div class="client" style="left:895px;top:438px"><i></i>Postwick</div>
</section>

<h2 class="sec-head" style="top:2068px">Text copy that explains<span>the value you provide to customers.</span></h2>

<article class="case" style="left:100px"><div class="ph" role="img" aria-label="Glowing blue server room corridor" style="background:linear-gradient(180deg,#0b2545,#2e8fd8)"></div><div class="tag"><i></i>DATAVAULT</div><h3>How to Align Your Application to the Optimal Infrastructure Enviroments</h3><hr><p>Lorem ipsum dolor sit onsectetur adipiscing elit, sed do eiusmod tempor incididunt</p></article>
<article class="case" style="left:443px"><div class="ph" role="img" aria-label="Modern domed building with a golden roof" style="background:linear-gradient(180deg,#3c5b8e,#b59a5e 60%,#d6d8dc)"></div><div class="tag"><i style="background:#222"></i>brandhold</div><h3>How to Align Your Application to the Optimal Infrastructure Enviroments</h3><hr><p>Lorem ipsum dolor sit onsectetur adipiscing elit, sed do eiusmod tempor incididunt</p></article>
<article class="case" style="left:784px"><div class="ph" role="img" aria-label="Aerial view of a lake among snowy mountains" style="background:linear-gradient(180deg,#d9dde2,#55697a 55%,#e4e7ea)"></div><div class="tag"><i style="background:#f5b731"></i>TALKLEDGER</div><h3>How to Align Your Application to the Optimal Infrastructure Enviroments</h3><hr><p>Lorem ipsum dolor sit onsectetur adipiscing elit, sed do eiusmod tempor incididunt</p></article>

<section class="contact">
  <h2 style="left:132px">Feel free to contact us with any questions. We’re happy to help</h2>
  <div class="btn" style="left:234px;top:230px;width:218px;height:47px">Get In Touch</div>
  <div class="divider"></div>
  <h2 style="left:652px">Editorial inspiration delivered straight to your inbox</h2>
  <div class="email">Email Address
    <svg width="20" height="18" viewBox="0 0 20 18"><path d="M0 8 L20 0 L14 18 L9 11 Z" fill="#4caf50"/></svg>
  </div>
</section>

<div class="footer-col abs" style="left:141px;top:3125px">
  <h4>CONTACT US</h4>
  <ul style="margin-top:12px">
    <li><svg width="9" height="12" viewBox="0 0 9 12"><path d="M4.5 0A4.5 4.5 0 0 0 0 4.5C0 8 4.5 12 4.5 12S9 8 9 4.5A4.5 4.5 0 0 0 4.5 0Z" fill="#222"/></svg>123 Your Adress Goes Here.<br>CA, 1234567</li>
    <li><svg width="11" height="11" viewBox="0 0 11 11"><path d="M2 0L4 3 3 4.5C4 6.5 5 7.5 6.5 8L8 7 11 9 9.5 11C4 10.5 .5 7 0 1.5Z" fill="#222"/></svg>888 888 8888</li>
    <li><svg width="12" height="10" viewBox="0 0 12 10"><rect width="12" height="10" fill="#222"/><path d="M0 0L6 5 12 0" stroke="#fff" fill="none"/></svg>info@lpstudio.net</li>
  </ul>
</div>
<div class="wordmark abs" style="left:515px;top:3150px">Larkfield Prose<br>Studio</div>
<div class="footer-col abs" style="left:880px;top:3125px">
  <h4>Follow Us</h4>
  <div class="social" style="margin-top:16px"><span aria-label="Social link"></span><span aria-label="Social link"></span><span aria-label="Social link"></span><span aria-label="Social link"></span></div>
</div>

<div class="copy">© 2021 Larkfield Prose Studio. Company</div>
</body>
</html>
```